Zorvalux Sports Performance Poster

We are in need of a poster for our upcoming summer Sports Performance Program during June and July.
This program caters to youth and teen athletes playing volleyball, soccer, and basketball.
Please see attached word document with program details for the poster.

MUST HAVES:
- Size needed 11x17 with bleeding for printing
- .PSD File Format WITH LAYERS (CS3 Compatible - Fonts included)*** A MUST
- Use Zorvalux Bootcamps Logo
- Use Information in the attached word doc

Requirements
Must have
• - Size needed 11x17 with bleeding for printing
• - .PSD File Format WITH LAYERS (CS3 Compatible - Fonts included)*** A MUST
• - Use Zorvalux Bootcamps Logo
• - Use Information in the attached word doc

```html
<!DOCTYPE html>
<html lang="en">
<head>
<meta charset="utf-8">
<title>Zorvalux Sports Performance Program</title>
<link rel="stylesheet" href="https://fonts.googleapis.com/css2?family=Open+Sans:wght@800&family=Source+Sans+3:wght@400;600;700&display=swap">
<style>
  :root {
    --blue-deep: #163f86;
    --blue-mid: #2458a8;
    --blue-light: #3a78c9;
    --navy: #14274d;
    --orange: #e9a559;
    --orange-soft: #f0b56c;
    --white: #ffffff;
  }
  html, body {
    margin: 0;
    padding: 0;
    width: 776px;
    height: 1200px;
    overflow: hidden;
    background: var(--blue-deep);
  }
  .poster {
    position: relative;
    width: 776px;
    height: 1200px;
    overflow: hidden;
    background: linear-gradient(180deg, var(--blue-mid) 0%, var(--blue-light) 45%, var(--blue-mid) 75%, var(--blue-deep) 100%);
    font-family: "Source Sans 3", sans-serif;
    color: var(--white);
  }
  .art {
    position: absolute;
    inset: 0;
  }
  .photo-volleyball {
    position: absolute;
    left: 0;
    top: 0;
    width: 240px;
    height: 980px;
    background: linear-gradient(180deg, rgba(214, 190, 205, 0.55) 0%, rgba(150, 140, 190, 0.45) 40%, rgba(60, 90, 160, 0.25) 75%, rgba(36, 88, 168, 0) 100%);
  }
  .photo-athlete {
    position: absolute;
    left: 370px;
    top: 295px;
    width: 406px;
    height: 905px;
    background: linear-gradient(180deg, rgba(190, 170, 150, 0.0) 0%, rgba(150, 145, 140, 0.55) 25%, rgba(60, 60, 70, 0.55) 65%, rgba(200, 200, 205, 0.4) 100%);
    border-radius: 160px 40px 0 120px;
  }
  .brand {
    position: absolute;
    left: 138px;
    top: 70px;
    display: flex;
    align-items: center;
    gap: 10px;
    font-family: "Source Sans 3", sans-serif;
    font-weight: 700;
    font-size: 27px;
    letter-spacing: 1px;
    color: var(--white);
    text-transform: uppercase;
  }
  .brand-mark {
    width: 18px;
    height: 18px;
    background: var(--orange);
  }
  .eyebrow {
    position: absolute;
    right: 44px;
    top: 42px;
    margin: 0;
    font-family: "Source Sans 3", sans-serif;
    font-weight: 600;
    font-size: 26px;
    letter-spacing: 5px;
    color: var(--orange);
  }
  .title {
    position: absolute;
    right: 40px;
    top: 80px;
    margin: 0;
    text-align: right;
    font-family: "Open Sans", sans-serif;
    font-weight: 800;
    font-size: 70px;
    line-height: 74px;
    letter-spacing: 1px;
    text-shadow: 0 3px 8px rgba(0, 0, 0, 0.35);
  }
  .title span { display: block; }
  .tagline {
    position: absolute;
    left: 175px;
    top: 340px;
    margin: 0;
    font-weight: 600;
    font-size: 35px;
    text-shadow: 0 2px 6px rgba(0, 0, 0, 0.3);
  }
  .ages-badge {
    position: absolute;
    left: 41px;
    top: 591px;
    width: 434px;
    height: 332px;
    border-radius: 50%;
    background: var(--navy);
    text-align: center;
  }
  .ages-heading {
    margin: 62px 0 0;
    font-weight: 600;
    font-size: 40px;
    line-height: 44px;
  }
  .ages-dates {
    margin: 14px 0 0;
    font-weight: 600;
    font-size: 24px;
    line-height: 31px;
  }
  .ages-dates sup { font-size: 14px; }
  .schedule {
    position: absolute;
    left: 65px;
    top: 972px;
    margin: 0;
  }
  .schedule-days {
    margin: 0 0 12px;
    font-weight: 600;
    font-size: 22px;
  }
  .schedule-list {
    margin: 0;
    padding: 0;
    list-style: none;
    font-weight: 600;
    font-size: 22px;
    line-height: 32px;
  }
  .schedule-list .track {
    display: inline-block;
    width: 58px;
  }
  .availability {
    margin: 12px 0 0;
    font-weight: 600;
    font-size: 23px;
  }
  .availability .highlight { color: var(--orange-soft); }
  .pricing {
    margin: 6px 0 0;
    font-weight: 600;
    font-size: 16px;
  }
</style>
</head>
<body>
<main class="poster">
  <svg class="art" width="776" height="1200" viewBox="0 0 776 1200" aria-hidden="true">
    <polygon points="455,318 776,300 776,1200 690,1200" fill="var(--orange)"/>
    <polygon points="316,430 350,438 322,450" fill="var(--white)"/>
    <polygon points="368,470 382,478 372,488" fill="var(--white)"/>
    <polygon points="360,510 395,492 385,540" fill="#2f6fd0"/>
    <polygon points="400,420 430,410 418,440" fill="var(--orange)"/>
    <polygon points="300,500 340,485 330,520" fill="#1f4fa0"/>
    <polygon points="335,545 350,555 338,562" fill="var(--orange)"/>
    <polygon points="418,688 436,680 432,698" fill="var(--orange)"/>
  </svg>

  <div class="photo-volleyball" role="img" aria-label="Photo of two volleyball players jumping at the net to block a ball"></div>
  <div class="photo-athlete" role="img" aria-label="Photo of a young basketball player dribbling a ball"></div>

  <div class="brand"><span class="brand-mark"></span>Zorvalux Bootcamps</div>

  <p class="eyebrow">Zorvalux’s</p>
  <h1 class="title"><span>SPORTS</span><span>PERFORMANCE</span><span>PROGRAM</span></h1>

  <p class="tagline">Speed | Agility | Power</p>

  <section class="ages-badge">
    <h2 class="ages-heading">AGES 8-17<br>YOUTH AND<br>TEEN PROGRAMS</h2>
    <p class="ages-dates">June 5<sup>th</sup> – 30<sup>th</sup><br>July 5<sup>th</sup> – 31<sup>st</sup></p>
  </section>

  <section class="schedule">
    <p class="schedule-days">Monday | Wednesday | Friday</p>
    <ul class="schedule-list">
      <li><span class="track">Youth</span>–&nbsp; 9:30-10:30am</li>
      <li><span class="track">Teen</span>–&nbsp; 10:30-11:30am</li>
      <li><span class="track">Teen</span>–&nbsp; 3:30-4:30pm</li>
    </ul>
    <p class="availability"><span class="highlight">Limited Space</span> – 15 spots per time track</p>
    <p class="pricing">$119 per month or $199 for both months</p>
  </section>
</main>
</body>
</html>
```